Visitenkarten und Briefpapier
Planung und Realisierung von individuellen und wertbeständigen Kamin- und Ofenlösungen, sowie Fliesen- und Baddesign.
Wir benötigen ein möglichst schlichtes Design für Visitenkarten, bzw. Briefpapier. Für die Visitenkarten gerne auch Vorschläge mit Prägung, Ausstanzung oder mit Heißfolie. Auch Klappkarten wären denkbar. Das Design soll "das gewisse Etwas haben" und nicht zu verspielt sein.
Die Visitenkarten sind für die Firma RUNK, das Logo von der Ausstellung "feldgrat" soll dezent mit eingebunden werden (bei dem Briefpapier z.B. in der Fußzeile". Die farbliche Gestaltung sollte sich an den Farben des Logos orientieren.
Schriftart für Texte: Century Gothic
Schriftfarbe: RAL 7016
Nur eine Idee: Ich könnte mir auch gut vorstellen, dass die Visitenkarte aus einer Zündholzverpackung (wenn dann aber eine besondere mit nur einem Zündholz oder einem besonders breiten) besteht: http://gluehfunk-muster.de/artikel_mappen.php

```html
<!DOCTYPE html>
<html lang="de">
<head>
<meta charset="utf-8">
<title>RUNK – Visitenkarte</title>
<link rel="stylesheet" href="https://fonts.googleapis.com/css2?family=Questrial&display=swap">
<style>
  :root {
    --page-bg: #8e8f90;
    --card-light: #dcdcdc;
    --card-dark: #1b262b;
    --ink: #383e42;
    --ink-strong: #15191c;
    --ink-soft: #6a6d70;
    --logo-light: #d3d3d3;
    --flame: #c8781c;
    --rule: #1f2b30;
  }
  * { box-sizing: border-box; margin: 0; padding: 0; }
  html, body { width: 1200px; height: 840px; overflow: hidden; }
  body {
    background: var(--page-bg);
    font-family: "Questrial", "Century Gothic", sans-serif;
    position: relative;
  }
  .card {
    position: absolute;
    top: 262px;
    width: 540px;
    height: 316px;
    border-radius: 22px;
    overflow: hidden;
    box-shadow: 0 6px 18px rgba(0,0,0,.25);
  }
  /* back side */
  .card--back { left: 40px; background: var(--card-dark); }
  .back-brand {
    position: absolute; left: 0; right: 0; top: 92px;
    text-align: center;
  }
  .back-brand__name {
    display: inline-flex; align-items: center; gap: 14px;
    font-size: 96px; letter-spacing: 6px; line-height: 1;
    color: var(--logo-light);
  }
  .brand-dot { width: 22px; height: 22px; border-radius: 50%; background: var(--flame); display: inline-block; }
  .back-brand__tag {
    margin-top: 10px; font-size: 27px; letter-spacing: 2px; color: var(--logo-light);
  }
  /* front side */
  .card--front { left: 620px; background: var(--card-light); color: var(--ink); }
  .front-brand { position: absolute; left: 30px; top: 36px; }
  .front-brand__name {
    display: flex; align-items: center; gap: 8px;
    font-size: 56px; letter-spacing: 4px; line-height: 1; color: var(--ink-strong);
  }
  .front-brand__name .brand-dot { width: 13px; height: 13px; }
  .front-brand__tag { margin-top: 4px; font-size: 16px; letter-spacing: 1px; color: var(--ink-strong); }
  .rule-main { position: absolute; left: 0; top: 140px; width: 330px; height: 2px; background: var(--rule); }
  .person { position: absolute; right: 30px; top: 72px; text-align: right; }
  .person__name {
    font-size: 25px; color: var(--ink-strong); letter-spacing: .5px;
    padding: 0 2px 4px 70px; border-bottom: 2px solid var(--rule);
  }
  .person__role { margin-top: 6px; font-size: 15px; color: var(--ink-soft); letter-spacing: .5px; }
  .contact { position: absolute; right: 26px; top: 184px; list-style: none; text-align: right; }
  .contact li {
    display: flex; justify-content: flex-end; align-items: center; gap: 10px;
    font-size: 17px; letter-spacing: 1.2px; color: var(--ink-soft); line-height: 27px;
  }
  .contact svg { width: 17px; height: 17px; fill: var(--ink-strong); }
  .address {
    position: absolute; left: 30px; bottom: 30px;
    font-size: 18px; letter-spacing: 1px; line-height: 22px; color: var(--ink-soft); font-style: normal;
  }
</style>
</head>
<body>

<section class="card card--back" aria-label="Rückseite der Visitenkarte">
  <div class="back-brand">
    <div class="back-brand__name">RUNK<span class="brand-dot"></span></div>
    <p class="back-brand__tag">kamine · öfen · fliesen</p>
  </div>
</section>

<section class="card card--front" aria-label="Vorderseite der Visitenkarte">
  <div class="front-brand">
    <div class="front-brand__name">RUNK<span class="brand-dot"></span></div>
    <p class="front-brand__tag">kamine · öfen · fliesen</p>
  </div>
  <div class="rule-main"></div>
  <div class="person">
    <p class="person__name">Lenard Hovik</p>
    <p class="person__role">Geschäftsführer</p>
  </div>
  <ul class="contact">
    <li>04417 / 38 91 20
      <svg viewBox="0 0 24 24" aria-label="Telefon"><path d="M6.6 10.8a15 15 0 0 0 6.6 6.6l2.2-2.2a1 1 0 0 1 1-.25 11.4 11.4 0 0 0 3.6.57 1 1 0 0 1 1 1V20a1 1 0 0 1-1 1A17 17 0 0 1 3 4a1 1 0 0 1 1-1h3.5a1 1 0 0 1 1 1c0 1.25.2 2.45.57 3.57a1 1 0 0 1-.25 1z"/></svg>
    </li>
    <li>04417 / 38 91 27
      <svg viewBox="0 0 24 24" aria-label="Fax"><path d="M7 3h10v4H7zM4 8h16a2 2 0 0 1 2 2v6h-4v5H6v-5H2v-6a2 2 0 0 1 2-2zm4 8v3h8v-3z"/></svg>
    </li>
    <li>info@runk-hellbrueck.de
      <svg viewBox="0 0 24 24" aria-label="E-Mail"><path d="M2 5h20v14H2zm2 2v.4l8 5.2 8-5.2V7zm0 2.8V17h16V9.8l-8 5.2z"/></svg>
    </li>
  </ul>
  <address class="address">Am Talgrund 12<br>35519 Hellbrück</address>
</section>

</body>
</html>
```